Invitation card to the opening of BRAVORA FITNESS CLUB

A successful training plan starts with BRAVORA Fitness!
Join us for our grand opening! OPEN HOUSE AND YOU ARE INVITED!
Tuesday 1st of August, 2017
Classes start from 7.30am till 9.30pm.
Explore the most fun, exciting, challenging and effective training system in the region.
Healthy drinks and delicious food will be provided.
We hope to see you there!

www.bravorafitnessclub.example
APP: BRAVORAFITQZN
Tel: 81-42 09 15

Industry/Entity Type

Fitness

Colors

Designer to choose colors to be used in the design.

Requirements
Must have
• Elegant card
Nice to have
• Logo in the background
Should not have
• pictures

```html
<!DOCTYPE html>
<html lang="en">
<head>
<meta charset="utf-8">
<title>Bravora Fitness Club – Grand Opening Invitation</title>
<link href="https://fonts.googleapis.com/css2?family=Cinzel:wght@400;600&family=Dancing+Script:wght@400&family=Open+Sans:ital,wght@0,400;1,400&display=swap" rel="stylesheet">
<style>
  :root {
    --backdrop: #e8e5e0;
    --paper: #f7f7f6;
    --charcoal: #48484a;
    --ink: #1b1b1b;
    --gold: #c8901f;
    --gold-line: #b0802a;
    --rule: #e2e2e0;
    --ghost: #ececea;
  }
  html, body {
    margin: 0;
    width: 1200px;
    height: 1200px;
    overflow: hidden;
    background: var(--backdrop);
  }
  .invitation {
    position: absolute;
    left: 218px;
    top: 60px;
    width: 764px;
    height: 1080px;
    background: var(--paper);
    box-shadow: 0 6px 24px rgba(0,0,0,0.18);
    overflow: hidden;
    font-family: "Open Sans", sans-serif;
    color: var(--ink);
  }
  .invitation__graphics {
    position: absolute;
    inset: 0;
  }
  .line {
    position: absolute;
    left: 0;
    right: 0;
    text-align: center;
    white-space: nowrap;
    margin: 0;
  }
  .brand__name {
    font-family: "Cinzel", serif;
    font-weight: 600;
    color: var(--ink);
    font-size: 60px;
    line-height: 60px;
    top: 228px;
    letter-spacing: 1px;
  }
  .brand__tag {
    font-family: "Cinzel", serif;
    font-weight: 600;
    color: var(--ink);
    font-size: 20px;
    line-height: 24px;
    top: 294px;
    letter-spacing: 10px;
    padding-left: 10px;
  }
  .tagline {
    font-family: "Dancing Script", cursive;
    font-size: 31px;
    line-height: 40px;
    top: 374px;
  }
  .tagline__brand { color: var(--gold); }
  .greeting {
    font-size: 28px;
    line-height: 36px;
    top: 472px;
  }
  .headline {
    font-family: "Cinzel", serif;
    font-weight: 400;
    color: var(--gold);
    font-size: 33px;
    line-height: 40px;
    top: 521px;
  }
  .schedule {
    font-size: 27px;
    line-height: 39px;
    top: 601px;
  }
  .pitch {
    font-style: italic;
    font-size: 20px;
    line-height: 31px;
    top: 716px;
  }
  .closing {
    font-family: "Dancing Script", cursive;
    font-size: 31px;
    line-height: 43px;
    top: 820px;
  }
  .divider {
    position: absolute;
    left: 0;
    right: 0;
    top: 940px;
    height: 2px;
    background: var(--rule);
  }
  .contact {
    color: var(--gold);
    font-size: 19px;
    line-height: 27px;
    top: 969px;
  }
</style>
</head>
<body>
  <article class="invitation">
    <svg class="invitation__graphics" viewBox="0 0 764 1080" width="764" height="1080" aria-hidden="true">
      <circle class="backdrop-ring" cx="385" cy="560" r="235" fill="none" stroke="var(--ghost)" stroke-width="22"/>
      <path class="header-band" d="M0,0 H764 V62 C660,34 560,54 440,104 C330,148 170,158 0,152 Z" fill="var(--charcoal)"/>
      <path class="header-edge" d="M0,156 C170,162 330,152 440,108 C560,58 660,38 764,66" fill="none" stroke="var(--gold-line)" stroke-width="4"/>
      <circle class="brand__mark" cx="382" cy="166" r="46" fill="none" stroke="var(--gold)" stroke-width="5"/>
    </svg>

    <h1 class="line brand__name">BRAVORA</h1>
    <p class="line brand__tag">FITNESS</p>

    <p class="line tagline">A successful training plan starts with <span class="tagline__brand">BRAVORA Fitness!</span></p>

    <p class="line greeting">Join us for our grand opening!</p>
    <p class="line headline">OPEN HOUSE AND YOU ARE INVITED!</p>

    <p class="line schedule">Tuesday 1st of August, 2017<br>Classes start from 7.30am till 9.30pm.</p>

    <p class="line pitch">Explore the most fun, exciting, challenging and<br>effective training system in the region.</p>

    <p class="line closing">Healthy drinks and delicious food will be provided.<br>We hope to see you there!</p>

    <div class="divider"></div>

    <p class="line contact">www.bravorafitnessclub.example<br>APP: BRAVORAFITQZN<br>Tel: 81-42 09 15</p>
  </article>
</body>
</html>
```